customer services company for the travel industry needs a flyer designed

we need a flyer for our London based company. We are an outsource service to the travel industry so our client companies receive a complaint from their customer about their holiday or travel arrangements and they pass it to us to handle. We take the stress and strain away from them that complaints present! check out our website www.harbourlinkassist.co.uk - blue features as our corporate colors. The business is 26 years old so well established in the industry. The reverse of the flyer will be printed with endorsements from current company clients. I would like something light hearted projecting the relief of pressure we can provide whilst also suggesting complaints and complainants will be in professional safe capable hands

Industry/Entity Type

Travel

```html
<!DOCTYPE html>
<html lang="en">
<head>
<meta charset="utf-8">
<title>Harbourlink Assist – Flyer</title>
<link href="https://fonts.googleapis.com/css2?family=Didact+Gothic&family=Open+Sans:wght@400;600;700;800&display=swap" rel="stylesheet">
<style>
:root{
  --sky:#2bb5ea;
  --sky-deep:#119fdc;
  --sky-pale:#d8f1fb;
  --navy:#1d2f72;
  --orange:#ef7d22;
  --white:#ffffff;
  --ink:#3a3f4a;
  --page:#e9edf1;
}
*{box-sizing:border-box;margin:0;padding:0}
html,body{width:1200px;height:994px;overflow:hidden;background:var(--page)}
body{position:relative;font-family:"Open Sans",sans-serif;color:var(--ink)}
.flyer{position:absolute;top:52px;width:420px;height:890px;background:var(--white);box-shadow:0 6px 22px rgba(20,40,70,.18);overflow:hidden;display:flex;flex-direction:column}
.flyer--front{left:150px}
.flyer--back{left:630px}

/* front */
.front-header{position:relative;height:222px;flex:none}
.brand{position:absolute;left:26px;top:22px;right:20px;z-index:2}
.brand__name{font-family:"Didact Gothic",sans-serif;font-size:38px;color:var(--navy);line-height:1}
.brand__tag{font-family:"Didact Gothic",sans-serif;font-size:14px;color:var(--navy);margin-top:4px;padding-left:70px}
.front-header__wave{position:absolute;inset:0}
.front-header__art{position:absolute;left:36px;top:108px;width:220px;height:84px;border-radius:40px;background:linear-gradient(100deg,#e9f7fd,#bfe6f7 60%,#1d5fa8);opacity:.9}
.badge{position:absolute;right:30px;top:128px;width:90px;height:90px;border-radius:50%;background:var(--white);border:6px solid var(--sky-deep);display:flex;flex-direction:column;align-items:center;justify-content:center;text-align:center;color:var(--navy);box-shadow:0 2px 6px rgba(0,0,0,.15)}
.badge__num{font-size:30px;font-weight:800;line-height:1}
.badge__label{font-size:8px;font-weight:700;letter-spacing:.4px;line-height:1.2;color:var(--orange);margin-top:2px}
.front-body{background:var(--sky);color:var(--white);padding:4px 28px 14px;flex:1;min-height:0;font-family:"Didact Gothic",sans-serif}
.clients__title{font-family:"Open Sans",sans-serif;font-weight:800;font-size:18px;margin-bottom:2px}
.clients__list{list-style:none;font-size:16px;line-height:1.38;padding-left:6px}
.clients__list li{display:flex;align-items:center;gap:10px}
.tick{width:13px;height:13px;flex:none}
.pitch{font-size:16px;line-height:1.35;text-align:center;margin-top:10px;padding-bottom:10px;border-bottom:1.5px solid rgba(255,255,255,.8)}
.services{text-align:center;font-size:15px;line-height:1.42;margin-top:9px}
.offer{background:var(--white);color:var(--navy);text-align:center;font-weight:800;font-size:14px;line-height:1.3;padding:9px 18px;flex:none}
.front-photos{height:100px;flex:none;display:flex}
.front-photos__img{flex:1}
.front-photos__img--ship{background:linear-gradient(180deg,#7cc3ef,#3b8fd0 60%,#1a5fa3)}
.front-photos__img--plane{background:linear-gradient(180deg,#5bb0ea,#d9eefb 70%,#a9d6f2)}
.front-footer{background:var(--sky-deep);color:var(--white);text-align:center;padding:10px 0 12px;flex:none}
.front-footer__web{font-family:"Didact Gothic",sans-serif;font-size:21px;line-height:1.3}
.front-footer__tel{font-weight:700;font-size:24px;letter-spacing:.5px;line-height:1.3}

/* back */
.reviews{padding:22px 28px 0;flex:none}
.reviews__title{color:var(--sky-deep);font-weight:800;font-size:16px;text-align:center;margin-bottom:6px}
.review{border-bottom:1.5px solid var(--sky);padding:6px 0 7px;font-size:11px;line-height:1.36}
.review__quote::before{content:"\201C";color:var(--sky-deep);font-weight:800;font-size:16px;line-height:0;margin-right:3px}
.review__quote::after{content:"\201D";color:var(--sky-deep);font-weight:800;font-size:16px;line-height:0;margin-left:2px}
.review__name{font-weight:700;text-transform:uppercase;margin-top:5px;font-size:10.5px}
.review__role{font-size:10.5px;line-height:1.3}
.review:last-child{border-bottom:none}
.contact{text-align:center;padding:4px 28px 12px;color:var(--navy);margin-top:auto}
.contact .brand__name{font-size:32px}
.contact .brand__tag{font-size:12.5px;padding-left:80px;text-align:left}
.contact__address{font-size:13px;line-height:1.35;margin-top:8px;color:var(--ink);text-align:right;padding-right:40px}
.contact__tel{font-weight:800;font-size:16px;color:var(--navy);margin-top:4px;text-align:right;padding-right:40px}
.back-footer{background:var(--sky-deep);color:var(--white);text-align:center;font-weight:700;font-size:18px;padding:11px 0;flex:none}
</style>
</head>
<body>

<article class="flyer flyer--front">
  <header class="front-header">
    <svg class="front-header__wave" viewBox="0 0 420 222" preserveAspectRatio="none" aria-hidden="true">
      <path d="M0 135 C120 195 270 150 420 95 L420 222 L0 222 Z" fill="var(--sky)"/>
      <path d="M0 168 C140 212 280 172 420 128 L420 222 L0 222 Z" fill="var(--sky-deep)" opacity=".25"/>
    </svg>
    <div class="brand">
      <div class="brand__name">Harbourlink Assist</div>
      <div class="brand__tag">Customer Service &amp; Training Specialists</div>
    </div>
    <div class="front-header__art" role="img" aria-label="Illustration of a cruise ship and a jet airliner over the sea"></div>
    <div class="badge">
      <span class="badge__num">26</span>
      <span class="badge__label">YEARS<br>EXPERIENCE</span>
    </div>
  </header>

  <section class="front-body">
    <h2 class="clients__title">We work with:</h2>
    <ul class="clients__list">
      <li><svg class="tick" viewBox="0 0 14 14"><path d="M1 7l4 4 8-9" fill="none" stroke="#fff" stroke-width="2.4"/></svg>Tour operators</li>
      <li><svg class="tick" viewBox="0 0 14 14"><path d="M1 7l4 4 8-9" fill="none" stroke="#fff" stroke-width="2.4"/></svg>Travel agents</li>
      <li><svg class="tick" viewBox="0 0 14 14"><path d="M1 7l4 4 8-9" fill="none" stroke="#fff" stroke-width="2.4"/></svg>Bed banks</li>
      <li><svg class="tick" viewBox="0 0 14 14"><path d="M1 7l4 4 8-9" fill="none" stroke="#fff" stroke-width="2.4"/></svg>Cruise lines</li>
      <li><svg class="tick" viewBox="0 0 14 14"><path d="M1 7l4 4 8-9" fill="none" stroke="#fff" stroke-width="2.4"/></svg>Coach companies</li>
      <li><svg class="tick" viewBox="0 0 14 14"><path d="M1 7l4 4 8-9" fill="none" stroke="#fff" stroke-width="2.4"/></svg>Airlines and dynamic packaging agents</li>
    </ul>
    <p class="pitch">Our professional, experienced team manage customer service issues and complaints for travel companies serving the UK markets.</p>
    <p class="services">Full outsourcing • Peak time support<br>Individual complaint handling<br>Ad hoc support • Up to date reporting</p>
  </section>

  <p class="offer">Complaints management services<br>Customer service training courses for the travel trade industry</p>

  <div class="front-photos">
    <div class="front-photos__img front-photos__img--ship" role="img" aria-label="Photo of a white cruise ship at sea"></div>
    <div class="front-photos__img front-photos__img--plane" role="img" aria-label="Photo of a passenger jet taking off"></div>
  </div>

  <footer class="front-footer">
    <div class="front-footer__web">www.harbourlinkassist.co.uk</div>
    <div class="front-footer__tel">+44 20 7946 0381</div>
  </footer>
</article>

<article class="flyer flyer--back">
  <section class="reviews">
    <h2 class="reviews__title">OUR HARD EARNED REPUTATION</h2>
    <div class="review">
      <p class="review__quote">Our members have made use of and appreciated the knowledge and experience of the team at Harbourlink Assist over many years. The training courses provided by Petra for GITF always receive very good reviews.</p>
      <p class="review__name">Maria Ellison</p>
      <p class="review__role">Partnership and Events Manager<br>Guild of Independent Travel Firms</p>
    </div>
    <div class="review">
      <p class="review__quote">It is great to have the support of Sarah and her colleagues when the going gets rough. Happily we do not have to call upon them often but we have received excellent service from them over the years when we have needed help. We are happy to endorse Harbourlink Assist.</p>
      <p class="review__name">Clara Denholm</p>
      <p class="review__role">Northern Rail Journeys</p>
    </div>
    <div class="review">
      <p class="review__quote">We have found the experience and knowledge of the team at Harbourlink Assist invaluable with the more complex claims that arise from time to time.</p>
      <p class="review__name">Tom Haverford</p>
      <p class="review__role">Head of Customer Support<br>Wayfarer Trips</p>
    </div>
    <div class="review">
      <p class="review__quote">We have worked with Harbourlink Assist for a number of years. The advice received has been excellent and their knowledge and experience are second to none. We would not hesitate to recommend their services as the company has proved an invaluable resource to us.</p>
      <p class="review__name">Anne Whitcombe</p>
      <p class="review__role">Managing Director<br>Alpine Lodge Breaks</p>
    </div>
    <div class="review">
      <p class="review__quote">We have been delighted with the access we have to such knowledgeable and friendly support. I have no hesitation in recommending Harbourlink Assist.</p>
      <p class="review__name">Karen Moss</p>
      <p class="review__role">Managing Director<br>Casa Sol Villas</p>
    </div>
  </section>

  <section class="contact">
    <div class="brand__name">Harbourlink Assist</div>
    <div class="brand__tag">Customer Service &amp; Training Specialists</div>
    <p class="contact__address">Unit 27 Quayside Studios<br>48-52 Ferry Lane<br>London • E14 9QT</p>
    <p class="contact__tel">Tel: +44 20 7946 0381</p>
  </section>

  <footer class="back-footer">www.harbourlinkassist.co.uk</footer>
</article>

</body>
</html>
```